Business card for Eyelash extension salon in Marisol Heights,California USA

We need new business card for our salon in Marisol Heights. The salon name is 'Lumarra' . We would like to have...Business name: Lumarra Name of person: will provide later Address 6128 N.Corbel Ridge Blvd Marisol Heights , CA 90999 Phone: will provide later (Text only) Web: www.lumarrastudio-example.com Pictogrid icon, Friendvale icon follow us for seasonal campaign and news @lumarrastudioexample Design should look elegant, high-end, clean, simple, cohesive with my brand. Please refer my brand board. Business name color will be metallic bronzy color. Im thinking grey background or white background. Thanks

Target Market(s)

25-35. Gender neutral. People who are in Entertainment business industry.
This is High-end Eyelash extension salon in Marisol Heights

Industry/Entity Type

Beauty Salon

Contact Information for Business Card

Business name: Lumarra
Name of person: will provide later
Address 6128 N.Corbel Ridge Blvd Marisol Heights , CA 90999
Phone: will provide later (Text only)
Web: www.lumarrastudio-example.com
Pictogrid icon, Friendvale icon
follow us for seasonal campaign and news @lumarrastudioexample

Requirements
Must have
• Beautiful, elegant, clean and simple look but very attractive and modern
Should not have
• We don't like too clutter, too busy designs.

```html
<!DOCTYPE html>
<html lang="en">
<head>
<meta charset="utf-8">
<title>Lumarra – Business Card</title>
<link rel="stylesheet" href="https://fonts.googleapis.com/css2?family=Cormorant+Garamond:wght@400;500&family=Josefin+Sans:wght@300;400&display=swap">
<style>
  :root {
    --page: #e6dccf;
    --bronze: #9c7a62;
    --band: #a0806a;
    --band-deep: #94735d;
    --marble-light: #f4f4f4;
    --marble-mid: #e2e2e3;
    --white: #ffffff;
    --serif: "Cormorant Garamond", Georgia, serif;
    --sans: "Josefin Sans", Arial, sans-serif;
  }
  * { box-sizing: border-box; margin: 0; padding: 0; }
  html, body { width: 1200px; height: 800px; overflow: hidden; }
  body { background: var(--page); position: relative; }

  .card {
    position: absolute;
    width: 560px;
    height: 320px;
    overflow: hidden;
    box-shadow: 0 6px 18px rgba(80, 60, 40, 0.18);
  }
  .marble {
    position: absolute;
    left: 0; right: 0;
    background: linear-gradient(130deg, var(--marble-light) 0%, var(--marble-mid) 35%, var(--marble-light) 55%, var(--marble-mid) 80%, var(--marble-light) 100%);
  }

  /* Front */
  .card-front { left: 60px; top: 240px; }
  .card-front .marble { top: 0; height: 224px; }
  .front-band {
    position: absolute; left: 0; right: 0; bottom: 0; height: 96px;
    background: var(--band);
    display: flex; align-items: center; justify-content: center;
  }
  .website {
    font-family: var(--serif); font-size: 20px; color: var(--white); letter-spacing: 0.5px;
  }
  .brand {
    position: absolute; left: 0; right: 0; top: 58px;
    text-align: center;
  }
  .brand-name {
    font-family: var(--serif); font-weight: 400; font-size: 84px; line-height: 1;
    color: var(--bronze); letter-spacing: 2px;
  }
  .brand-place {
    display: block; margin: 10px 0 0 250px;
    font-family: var(--sans); font-weight: 300; font-size: 11px; letter-spacing: 3px;
    color: var(--bronze);
  }

  /* Back (set landscape, turned upright) */
  .card-back {
    left: 640px; top: 240px;
    transform: rotate(90deg);
  }
  .back-photo {
    position: absolute; left: 0; right: 0; top: 0; height: 228px;
    background: radial-gradient(ellipse at 70% 40%, #a98a74 0%, var(--band) 45%, var(--band-deep) 100%);
  }
  .card-back .marble { bottom: 0; height: 92px; }
  .person {
    position: absolute; left: 40px; top: 40px; width: 184px;
    font-family: var(--sans); font-weight: 300; font-size: 15px; letter-spacing: 1.5px;
    color: var(--white);
    padding-bottom: 10px;
    border-bottom: 1px solid var(--white);
  }
  .address {
    position: absolute; left: 224px; top: 40px;
    font-family: var(--serif); font-style: normal; font-size: 16px; line-height: 1.3;
    color: var(--white);
    padding: 36px 0 0 16px;
    border-left: 1px solid var(--white);
  }
  .social {
    position: absolute; left: 0; right: 0; bottom: 0; height: 92px;
    display: flex; flex-direction: column; align-items: center; justify-content: center; gap: 8px;
    color: var(--bronze);
  }
  .networks { display: flex; gap: 18px; font-family: var(--serif); font-size: 12px; }
  .network { display: flex; align-items: center; gap: 5px; }
  .network-dot { width: 10px; height: 10px; border-radius: 50%; background: var(--bronze); }
  .follow { font-family: var(--serif); font-size: 16px; letter-spacing: 0.3px; }
</style>
</head>
<body>

  <section class="card card-front">
    <div class="marble" role="img" aria-label="White and grey marble texture"></div>
    <div class="brand">
      <div class="brand-name">Lumarra</div>
      <span class="brand-place">MARISOL HEIGHTS</span>
    </div>
    <div class="front-band">
      <p class="website">www.lumarrastudio-example.com</p>
    </div>
  </section>

  <section class="card card-back">
    <div class="back-photo" role="img" aria-label="Bronze-toned close-up photo of lash extensions"></div>
    <p class="person">NAME OF PERSON</p>
    <address class="address">
      6128 N.Corbel Ridge Blvd<br>
      Marisol Heights<br>
      CA 90999<br>
      Phone (Text only)
    </address>
    <div class="marble" role="img" aria-label="White and grey marble texture"></div>
    <div class="social">
      <div class="networks">
        <span class="network"><span class="network-dot"></span>Friendvale</span>
        <span class="network"><span class="network-dot"></span>Pictogrid</span>
      </div>
      <p class="follow">follow us for seasonal campaign and news @lumarrastudioexample</p>
    </div>
  </section>

</body>
</html>
```